Create a Business Card Design Project for a new logistics company

We need a business card designed for a new company in Australia.

Type of business is logistics/trucking.

Medium will be brushed black metal card that can/will be acid etched to a brushed steel silver, acid die cut and two printed colours of our choice which will be white and pantone orange.

We have hopes that the design will be simple, modern and represent with a quick glance what our company does.

Please read instructions carefully in must have box any questions please ask.

If you are interested in this job please look at other job that we have which is very similar with logo and design

Please have a look at the things that can be done with metals cards on google images for inspiration.

Target Market(s)

Men from 20yrs of age to 60yrs of age

Industry/Entity Type

Steel

Requirements
Must have
• Must Have:
- Front of card:

Must use the company logo and name provided as attachment (see below KVR-black-background-cmyk).
Logo grey will be etched, orange and white will be printed on card. Parts of the logo could even be die cut.

The word -Logistics anytime, anywhere- on front etched, printed or die cut.

detail needed on front or back depending on your design layout.

Name
position
email
mobile

all details can be on front if a nice design is etched on the back of card or to keep front simple you can put all detail on back of card, I will leave the lay out to you.

Colours in logo are

Pantone 144 C Orange
Pantone 11-0601 White
Pantone 7539 C Gray
Pantone 426 C Black

However black will be the base of black metal card. Gray will be replaced with the etching in card revealing the silver. Orange and white will be printed on card.

have fun!!
Nice to have
• The file attached called idea is just an example of what can be designed and etched into card. Google has many more idea's for metal business cards.
Should not have
• Please don't clutter the card
No fonts smaller then 7 points

```html
<!DOCTYPE html>
<html lang="en">
<head>
<meta charset="utf-8">
<title>KVR Business Card</title>
<link href="https://fonts.googleapis.com/css2?family=Arimo:wght@400;700&display=swap" rel="stylesheet">
<style>
  :root {
    --stage: #2a2a2a;
    --card-black: #0f0f10;
    --card-edge: #1c1c1e;
    --orange: #f08a1c;
    --white: #f4f4f2;
    --steel: #a9abad;
    --steel-dim: #7d7f82;
  }
  * { box-sizing: border-box; margin: 0; padding: 0; }
  html, body { width: 1200px; height: 872px; overflow: hidden; }
  body {
    background: var(--stage);
    font-family: "Arimo", Arial, sans-serif;
    display: flex; align-items: center; justify-content: center; gap: 48px;
  }
  .card {
    width: 520px; height: 300px; border-radius: 22px;
    background: linear-gradient(160deg, var(--card-edge), var(--card-black) 60%);
    position: relative; overflow: hidden;
    box-shadow: 0 10px 30px rgba(0,0,0,.45);
  }
  .wordmark { display: flex; align-items: center; gap: 12px; }
  .wordmark-square { width: 22px; height: 22px; background: var(--steel); }
  .wordmark-name { font-weight: 700; color: var(--orange); letter-spacing: 2px; line-height: 1; }
  .tagline { position: absolute; color: var(--white); text-transform: uppercase; white-space: nowrap; }
  .wordmark-rule { position: absolute; height: 2px; background: var(--steel-dim); }

  /* front */
  .card-front .wordmark { position: absolute; left: 120px; top: 96px; }
  .card-front .wordmark-name { font-size: 60px; }
  .card-front .tagline { left: 120px; top: 166px; font-size: 13px; letter-spacing: 2.5px; }
  .card-front .wordmark-rule { left: 120px; top: 190px; width: 290px; }
  .card-front .web {
    position: absolute; left: 0; right: 0; bottom: 42px; text-align: center;
    color: var(--steel); font-size: 16px; letter-spacing: 9px;
  }

  /* back */
  .card-back .wordmark { position: absolute; left: 34px; top: 100px; }
  .card-back .wordmark-square { width: 16px; height: 16px; }
  .card-back .wordmark-name { font-size: 40px; }
  .card-back .tagline { left: 34px; top: 148px; font-size: 9.5px; letter-spacing: 1.2px; }
  .card-back .wordmark-rule { left: 34px; top: 166px; width: 196px; }
  .divider { position: absolute; left: 248px; top: 48px; bottom: 48px; width: 1px; background: var(--steel-dim); }
  .details { position: absolute; left: 268px; top: 50px; right: 20px; }
  .person-name { color: var(--orange); font-size: 22px; font-weight: 400; }
  .person-role { color: var(--white); font-size: 12px; margin-top: 4px; }
  .contact-list { list-style: none; margin-top: 22px; }
  .contact-list li {
    display: flex; align-items: flex-start; gap: 9px;
    color: var(--steel); font-size: 12.5px; line-height: 1.25; margin-bottom: 5px;
  }
  .contact-list svg { width: 12px; height: 12px; flex: none; margin-top: 1px; fill: var(--orange); }
</style>
</head>
<body>
  <section class="card card-front" aria-label="Card front">
    <div class="wordmark">
      <span class="wordmark-square"></span>
      <span class="wordmark-name">KVR</span>
    </div>
    <p class="tagline">Logistics anytime, anywhere</p>
    <div class="wordmark-rule"></div>
    <p class="web">www.kvr.com.au</p>
  </section>

  <section class="card card-back" aria-label="Card back">
    <div class="wordmark">
      <span class="wordmark-square"></span>
      <span class="wordmark-name">KVR</span>
    </div>
    <p class="tagline">Logistics anytime, anywhere</p>
    <div class="wordmark-rule"></div>
    <div class="divider"></div>
    <div class="details">
      <h1 class="person-name">Jordan Hale</h1>
      <p class="person-role">CEO and President</p>
      <ul class="contact-list">
        <li><svg viewBox="0 0 12 12"><path d="M6 0a4 4 0 0 0-4 4c0 3 4 8 4 8s4-5 4-8a4 4 0 0 0-4-4zm0 5.5A1.5 1.5 0 1 1 6 2.5a1.5 1.5 0 0 1 0 3z"/></svg><span>12 Sample Road,<br>Northgate, QLD 4013</span></li>
        <li><svg viewBox="0 0 12 12"><path d="M2 1h3l1 3-1.5 1a7 7 0 0 0 2.5 2.5L8 6l3 1v3a1 1 0 0 1-1 1A9 9 0 0 1 1 2a1 1 0 0 1 1-1z"/></svg><span>800-555-0142</span></li>
        <li><svg viewBox="0 0 12 12"><rect x="3" y="0" width="6" height="12" rx="1"/></svg><span>651-555-0187</span></li>
        <li><svg viewBox="0 0 12 12"><rect x="0" y="3" width="12" height="8" rx="1"/><rect x="3" y="0" width="6" height="3"/></svg><span>651-555-0163</span></li>
        <li><svg viewBox="0 0 12 12"><path d="M0 2h12v8H0zm1 1 5 4 5-4"/></svg><span>hello@kvr.com.au</span></li>
        <li><svg viewBox="0 0 12 12"><circle cx="6" cy="6" r="6"/></svg><span>www.kvr.com.au</span></li>
      </ul>
    </div>
  </section>
</body>
</html>
```